ZentaLOOM new era @ Hyper Digitalization

We need a Brochure that show all our product, services and consulting related to Hyper Digitalization into the industrial internet of things world.
We need a document that can be handled as a electronic brochure, this means that we need to show strong corporate presence, with strong skill of technology, and we have credentials and key sucess projects related to Manufacturing industries.
Key industries that we attend: Automotive, Chemical, Food and Beverage, Mining, Paper and Pulp, Oil and Gas, Energy Management.
We save money to our customer in 6 ways: 1) Eficiency in operation 2) Production Control 3) Hyper Digitalization of Thing Optimizing asset ussage 4) Maintenance and predictive of assets risks 5) Quality Control reducing Cost 6) Augmented Reality in operation and control
Target Market(s)
Manufacturing Industry. CEO of companies that has challenges of saving operation costs into plants of manufacturing.
Industry/Entity Type
Software
Font styles to use
Other font styles liked:
- MONTSERRAT
Requirements
Must have
- Technology Enviroment, our logo, our expertise, simple message about what our company does and the DNA, infography of the company, cases of sucess, cases of savings $ using our tecnology and services, what we can do for the customer in a few words
Nice to have
- standarize our colors related to our presentation, futuristic, information related to Artificial Inteligence related to machinery
Should not have
- old version of technology,

```html
<!DOCTYPE html>
<html lang="en">
<head>
<meta charset="utf-8">
<title>ZentaLOOM — Hyper Digitalization Brochure</title>
<link href="https://fonts.googleapis.com/css2?family=Montserrat:wght@400;500;600;700&display=swap" rel="stylesheet">
<style>
:root{
  --navy:#1d5fab;
  --deep:#123f7a;
  --sky:#4bb4d8;
  --pale:#cfe9f3;
  --ink:#2b2b2b;
  --mute:#8a8f96;
  --white:#ffffff;
}
*{margin:0;padding:0;box-sizing:border-box}
html,body{width:1200px;height:883px;overflow:hidden}
body{background:linear-gradient(180deg,#8c8c8c 0%,#b2b2b2 55%,#c6c6c6 100%);font-family:'Montserrat',sans-serif;color:var(--ink);position:relative}
.page{position:absolute;width:241px;height:341px;background:var(--white);overflow:hidden;box-shadow:0 8px 14px rgba(0,0,0,.28)}
.abs{position:absolute}
.fill-navy{background:var(--navy)}
.fill-sky{background:var(--sky)}
.photo{position:absolute}
.photo-blue{background:radial-gradient(circle at 70% 40%,rgba(120,210,245,.75),transparent 45%),radial-gradient(circle at 25% 75%,rgba(60,150,220,.6),transparent 50%),linear-gradient(135deg,#0c3570,#1e66b0 55%,#2f8ccc)}
.photo-dark{background:radial-gradient(circle at 55% 45%,rgba(110,200,240,.7),transparent 40%),linear-gradient(160deg,#071f45,#15498a 60%,#2a78b8)}
.photo-warm{background:radial-gradient(circle at 65% 35%,rgba(240,190,90,.8),transparent 40%),radial-gradient(circle at 25% 70%,rgba(60,90,140,.7),transparent 50%),linear-gradient(135deg,#39465c,#8a6a48 55%,#c99440)}
.photo-grey{background:radial-gradient(circle at 40% 35%,rgba(235,242,248,.9),transparent 45%),radial-gradient(circle at 75% 75%,rgba(40,80,130,.6),transparent 45%),linear-gradient(135deg,#b6c4d2,#7f95ad 60%,#4c6a8c)}
.photo-teal{background:radial-gradient(circle at 75% 60%,rgba(230,170,150,.55),transparent 35%),radial-gradient(circle at 20% 40%,rgba(90,200,230,.7),transparent 45%),linear-gradient(180deg,#0b3350,#1c6a8c 55%,#4aaac4)}
.framed{border:1.5px solid var(--white)}
.h{font-weight:700;color:var(--navy);font-size:8.5px;line-height:1}
.h-sky{color:var(--sky)}
.h-white{color:var(--white)}
.h-sm{font-size:6px;font-weight:600;color:var(--sky);line-height:1.05}
.txt{font-size:3.5px;line-height:1.3;color:var(--ink)}
.txt-w{color:var(--white)}
.list{list-style:none;font-size:3.6px;line-height:1.25}
.list li{position:relative;padding-left:5px;margin-bottom:2.9px}
.list li::before{content:"";position:absolute;left:0;top:.6px;border-left:2.4px solid var(--navy);border-top:1.4px solid transparent;border-bottom:1.4px solid transparent}
.list-w li{color:var(--white)}
.list-w li::before{border-left-color:var(--white)}
.brand{font-weight:600;color:var(--navy);letter-spacing:.2px}
.web{font-size:3.6px;color:var(--mute)}
.ring{position:absolute;width:44px;height:29px;border-radius:50%;background:#9a9a9a;box-shadow:0 3px 0 #7a7a7a}
.ring span{position:absolute;left:4px;top:3px;width:36px;height:20px;border-radius:50%;background:var(--white);display:flex;align-items:center;justify-content:center;text-align:center;font-size:4px;font-weight:700;line-height:1}
.ring.blue{background:var(--navy);box-shadow:0 3px 0 #0f3d78}
.ring-list{position:absolute;left:86px;list-style:none;font-size:2.7px;line-height:1;color:var(--ink)}
.ring-list li{margin-bottom:3.4px;position:relative}
.ring-list li::before{content:"";position:absolute;left:-13px;top:1.3px;width:11px;border-top:.5px solid var(--sky)}
.tile{position:absolute;width:24px;height:19px}
.tile-lbl{position:absolute;font-size:3.5px}
.quote{position:absolute;left:0;width:241px;padding:4px 16px 0}
.quote p{font-size:3.5px;line-height:1.25}
.quote b{display:block;font-size:3.5px;font-weight:700;margin-top:2px}
.q-sky{background:var(--pale)}
.q-pale{background:#eaf5fa}
</style>
</head>
<body>

<section class="page" style="left:53px;top:58px">
  <div class="photo photo-blue" style="left:0;top:59px;width:241px;height:210px" role="img" aria-label="Blue digital globe with network lines"></div>
  <div class="abs fill-sky" style="left:0;top:269px;width:241px;height:14px"></div>
  <div class="photo photo-dark framed" style="left:15px;top:30px;width:63px;height:64px" role="img" aria-label="Hands on laptop with digital overlay"></div>
  <div class="photo photo-warm framed" style="left:15px;top:102px;width:63px;height:63px" role="img" aria-label="Engineer with tablet in plant"></div>
  <div class="photo photo-grey framed" style="left:15px;top:174px;width:63px;height:64px" role="img" aria-label="Robotic production line"></div>
  <div class="photo photo-grey framed" style="left:15px;top:247px;width:63px;height:63px" role="img" aria-label="Hand drawing a data chart"></div>
  <h1 class="abs h-white" style="right:13px;top:191px;font-size:11px;font-weight:700;line-height:.92;text-align:right">Connecting<br>machines,<br>users and data.</h1>
  <p class="abs web" style="left:15px;top:317px">www.zentaloom-mx.com</p>
  <p class="abs brand" style="right:15px;top:310px;font-size:10.5px">ZentaLOOM</p>
</section>

<section class="page" style="left:337px;top:58px">
  <div class="abs fill-navy" style="left:88px;top:0;width:153px;height:92px"></div>
  <h2 class="abs h" style="left:15px;top:11px">About Us</h2>
  <p class="abs txt" style="left:15px;top:24px;width:44px">We are specialists in automation, process control, information technologies, development and consulting for quality, efficiency and production.<br><br>Our goal is to always provide the best solutions in conjunction with our technology partners, Orvana &amp; Linkware.</p>
  <h2 class="abs h h-sky" style="left:101px;top:11px">Our DNA</h2>
  <p class="abs txt txt-w" style="left:101px;top:24px;width:122px">We want all companies to operate in an automated way, to be more efficient and to compete with whoever is globally. We have the knowledge and experience to achieve it.</p>
  <h3 class="abs h-sm" style="left:101px;top:41px">Our commitments:</h3>
  <ul class="abs list list-w" style="left:95px;top:53px;width:135px;line-height:1.3">
    <li style="margin-bottom:5px">Improve the operation of each company individually.</li>
    <li style="margin-bottom:5px">Impact the country's competitiveness</li>
    <li>Support companies to access the highest levels of development, productivity, financing and profitability.</li>
  </ul>
  <h3 class="abs h-sm" style="left:15px;top:101px">Smart<br>Machines</h3>
  <p class="abs txt" style="left:15px;top:116px;width:62px">Intelligent machines in operation and control, in the same synchronization regardless of the brand installed. Efficiency that saves in operation. Creating brilliant machines.</p>
  <div class="abs" style="left:82px;top:101px;height:49px;border-left:.6px solid var(--sky)"></div>
  <h3 class="abs h-sm" style="left:88px;top:101px">Operational<br>Excellence</h3>
  <p class="abs txt" style="left:88px;top:116px;width:62px">Operational excellence is part of our language, strengthening the ties of efficiency in the company delivers revolutionary results. Saving and producing is easy with the experts.</p>
  <div class="abs" style="left:155px;top:101px;height:49px;border-left:.6px solid var(--sky)"></div>
  <h3 class="abs h-sm" style="left:160px;top:101px">Industrial<br>Internet</h3>
  <p class="abs txt" style="left:160px;top:116px;width:62px">Extending the Internet to industrial operation will exceed global energy savings by more than 1 Billion USD. A new generation of systems emerges, be part of this revolution.</p>
  <div class="photo photo-grey" style="left:15px;top:156px;width:67px;height:51px" role="img" aria-label="Technicians with robotic equipment"></div>
  <div class="photo photo-warm" style="left:88px;top:156px;width:67px;height:51px" role="img" aria-label="Worker in safety vest with laptop"></div>
  <div class="photo photo-dark" style="left:160px;top:156px;width:67px;height:51px" role="img" aria-label="Light trails of data in motion"></div>
  <div class="abs fill-sky" style="left:88px;top:213px;width:153px;height:14px"></div>
  <div class="photo photo-teal" style="left:0;top:227px;width:241px;height:114px" role="img" aria-label="Businessman holding phone over city network overlay"></div>
  <p class="abs" style="left:15px;top:318px;background:var(--white);padding:1.5px 4px;font-size:7.5px;font-weight:500;color:var(--navy)">Linkware</p>
  <p class="abs" style="right:15px;top:317px;font-size:9px;font-weight:500;color:var(--white);letter-spacing:.5px">ORVANA</p>
</section>

<section class="page" style="left:622px;top:58px">
  <h2 class="abs h" style="left:15px;top:10px">Consulting Strategy</h2>
  <ul class="abs list" style="left:10px;top:23px;width:125px;font-size:3.4px">
    <li>We know that all customers are in different maturity level of digitalization.</li>
    <li>Our Strategy helps to start simple, low cost and produce big changes</li>
  </ul>
  <div class="photo photo-grey" style="left:145px;top:0;width:96px;height:105px" role="img" aria-label="Engineer in lab coat beside server cabinet"></div>
  <div class="photo" style="left:145px;top:111px;width:96px;height:230px;background:radial-gradient(circle at 70% 30%,rgba(200,240,255,.7),transparent 40%),radial-gradient(circle at 30% 80%,rgba(30,120,190,.55),transparent 45%),linear-gradient(160deg,#3fa9d6,#7fd0ec 50%,#3a9fd0)" role="img" aria-label="Light blue network mesh background"></div>
  <p class="abs" style="left:170px;top:305px;transform:rotate(-90deg);transform-origin:0 0;font-size:26px;font-weight:500;color:rgba(255,255,255,.55);white-space:nowrap">Industry 4.0</p>
  <svg class="abs" style="left:28px;top:50px" width="22" height="291" viewBox="0 0 22 291"><polygon points="11,0 22,12 16,12 16,291 6,291 6,12 0,12" fill="#c4c4c4"/></svg>
  <div class="abs" style="left:44px;top:66px;width:95px;height:40px;border:.6px solid #9a9a9a;background:var(--white)"></div>
  <ul class="abs list" style="left:46px;top:70px;width:90px;font-size:3.5px;line-height:1.15">
    <li style="margin-bottom:2px">We analyse actual situation in operations</li>
    <li style="margin-bottom:2px">We drive digital project to gain performance</li>
    <li>Steps understanding the level of maturity</li>
  </ul>
  <div class="ring" style="left:17px;top:107px"><span>Industry 4.0</span></div>
  <ul class="ring-list" style="top:112px"><li>Datascience</li><li>Analytics</li><li>Predictive &amp; Prescriptive</li><li>Consulting Services</li></ul>
  <div class="ring blue" style="left:17px;top:142px"><span>Interconected</span></div>
  <ul class="ring-list" style="top:147px"><li>API Rest, MQTT.</li><li>Web Services</li><li>ERP Connect</li><li>Cybersecurity</li></ul>
  <div class="ring" style="left:17px;top:178px"><span>Storaging</span></div>
  <ul class="ring-list" style="top:185px"><li>Historian</li><li>Other sources noSQL Timeseries</li><li>BigData</li></ul>
  <div class="ring blue" style="left:17px;top:213px"><span>Automated</span></div>
  <ul class="ring-list" style="top:218px"><li>HMI SCADA Suite</li><li>Augmented Reality</li><li>Industrial digitalization</li><li>Workflow prescriptive</li></ul>
  <div class="ring" style="left:17px;top:248px"><span>Intrumented</span></div>
  <ul class="ring-list" style="top:253px"><li>HMI low cost</li><li>Manual Input</li><li>Workflow Instructions</li><li>Condition Base Monitoring</li></ul>
  <div class="ring blue" style="left:17px;top:284px"><span>Manual<br>Operations</span></div>
  <ul class="ring-list" style="top:292px"><li>Partner ecosystem</li><li>Labor electrical &amp; mechanical<br>job by SI</li></ul>
  <div class="abs" style="left:44px;top:319px;width:95px;height:14px;border:.6px solid #9a9a9a;background:var(--white)"></div>
  <ul class="abs list" style="left:46px;top:321px;width:90px;font-size:3.5px;line-height:1.1"><li>Step by step, our customer starts gaining optimization in different ways</li></ul>
  <div class="abs fill-navy" style="left:0;top:330px;width:25px;height:11px"></div>
</section>

<section class="page" style="left:905px;top:58px">
  <div class="photo photo-grey" style="left:0;top:0;width:241px;height:145px" role="img" aria-label="Hand holding a glowing digital globe"></div>
  <div class="abs fill-sky" style="left:73px;top:131px;width:168px;height:14px"></div>
  <div class="photo photo-dark framed" style="left:15px;top:96px;width:58px;height:58px" role="img" aria-label="Digital circuit tunnel"></div>
  <div class="photo photo-dark" style="left:15px;top:162px;width:57px;height:56px" role="img" aria-label="Finger touching a holographic dial"></div>
  <h2 class="abs h" style="left:86px;top:154px">Our Services</h2>
  <ul class="abs list" style="left:81px;top:168px;width:150px;font-size:3.6px">
    <li style="margin-bottom:3.5px">OT interconnectivity for operations</li>
    <li style="margin-bottom:3.5px">HMI &amp; MES Support</li>
    <li style="margin-bottom:3.5px">Digital Production Process Optimization</li>
    <li style="margin-bottom:3.5px">Migration services</li>
    <li style="margin-bottom:3.5px">PLC &amp; PAC Control System Support</li>
    <li>Annual Support &amp; Outsourcing plant Engineers</li>
  </ul>
  <h2 class="abs h" style="left:86px;top:224px">Industries we serve</h2>
  <div class="tile fill-navy" style="left:86px;top:236px"></div><p class="tile-lbl" style="left:117px;top:244px">Petrochemistry</p>
  <div class="tile fill-navy" style="left:159px;top:236px"></div><p class="tile-lbl" style="left:188px;top:244px">Water and Treatment</p>
  <div class="tile fill-sky" style="left:86px;top:258px"></div><p class="tile-lbl" style="left:117px;top:266px">Automotive</p>
  <div class="tile fill-sky" style="left:159px;top:258px"></div><p class="tile-lbl" style="left:188px;top:266px">Mining and Metals</p>
  <div class="tile fill-navy" style="left:86px;top:281px"></div><p class="tile-lbl" style="left:117px;top:289px">Life sciences</p>
  <div class="tile fill-navy" style="left:159px;top:281px"></div><p class="tile-lbl" style="left:188px;top:289px">Energy</p>
  <div class="tile fill-sky" style="left:86px;top:303px"></div><p class="tile-lbl" style="left:117px;top:311px">Food and drinks</p>
  <div class="tile fill-sky" style="left:159px;top:303px"></div><p class="tile-lbl" style="left:188px;top:311px">Aerospace</p>
  <div class="abs fill-navy" style="left:0;top:327px;width:73px;height:14px"></div>
</section>

<section class="page" style="left:53px;top:455px">
  <h2 class="abs h" style="left:16px;top:15px">Products</h2>
  <p class="abs txt" style="left:16px;top:29px">Hardware &amp; Software for industrial operations</p>
  <h3 class="abs h-sm" style="left:16px;top:37px;font-size:5.5px">Software representatives:</h3>
  <ul class="abs list" style="left:10px;top:46px;font-size:3.6px"><li>Orvana</li><li>Kestrel Linkware</li><li>Emberline</li><li>OPC Raylink</li><li>Brightbyte</li></ul>
  <h3 class="abs h-sm" style="left:16px;top:96px;font-size:5.5px">Hardware representatives:</h3>
  <ul class="abs list" style="left:10px;top:104px;font-size:3.6px"><li>Norvik Automation</li><li>Emberline</li><li>Vantrix Computers</li><li>SDT Comm</li></ul>
  <div class="photo photo-warm" style="left:121px;top:0;width:120px;height:130px" role="img" aria-label="Technician with tablet beside yellow robot arm"></div>
  <div class="abs fill-sky" style="left:121px;top:130px;width:120px;height:11px"></div>
  <div class="photo photo-dark" style="left:0;top:141px;width:241px;height:102px" role="img" aria-label="Hand on tablet with globe and security icons"></div>
  <div class="abs fill-navy" style="left:0;top:243px;width:121px;height:98px"></div>
  <h2 class="abs h h-sky" style="left:16px;top:254px">Consulting</h2>
  <ul class="abs list list-w" style="left:10px;top:267px;width:108px;font-size:3.6px;line-height:1.2">
    <li style="margin-bottom:4px">Data Science and Analytics</li>
    <li style="margin-bottom:4px">AI &amp; Machine Learning techniques for OT users</li>
    <li style="margin-bottom:4px">Datalakes &amp; Data preparation for IIOT</li>
    <li style="margin-bottom:4px">Batch Hybrid process</li>
    <li>Data Tuning</li>
  </ul>
  <h2 class="abs h" style="left:136px;top:254px">Training</h2>
  <p class="abs txt" style="left:136px;top:267px">Training center &amp; courses:</p>
  <ul class="abs list" style="left:130px;top:275px;width:105px;font-size:3.6px;line-height:1.2">
    <li style="margin-bottom:4px">Linkware OPC</li>
    <li style="margin-bottom:4px">HMI SCADA Stellaware Touchview</li>
    <li style="margin-bottom:4px">Norvik Vista, Simplexa, Plant Suite</li>
    <li style="margin-bottom:4px">PLC Programming</li>
    <li style="margin-bottom:4px">IIOT Platforms</li>
    <li>Machine Learning Platforms</li>
  </ul>
</section>

<section class="page" style="left:337px;top:455px;background:radial-gradient(circle at 85% 60%,rgba(90,170,235,.6),transparent 35%),radial-gradient(circle at 90% 10%,rgba(70,140,220,.5),transparent 30%),linear-gradient(160deg,#0a2a66,#1a4f9c 55%,#0e3474)" role="img" aria-label="Deep blue digital data background">
  <div class="abs" style="left:0;top:20px;width:180px;height:253px;background:#3fa6d4"></div>
  <h2 class="abs h h-white" style="left:15px;top:30px">Orvana Software Line</h2>
  <ul class="abs list list-w" style="left:9px;top:46px;width:130px;font-size:3.6px;line-height:1.2">
    <li style="margin-bottom:4.6px">Orvana HMI &amp; Control. HMI SCADA</li>
    <li style="margin-bottom:4.6px">Orvana Process Optimization. Workflow &amp; MES Systems</li>
    <li>Orvana Asset Performance Management. APM</li>
  </ul>
  <h2 class="abs h h-white" style="left:15px;top:100px">Linkware Software Line</h2>
  <ul class="abs list list-w" style="left:9px;top:116px;width:130px;font-size:3.6px;line-height:1.2">
    <li style="margin-bottom:4.6px">Industrial Connectivity. OPC Servers &amp; Drivers</li>
    <li style="margin-bottom:4.6px">Industrial IOT</li>
    <li style="margin-bottom:4.6px">Machine to Machine Connectivity</li>
    <li style="margin-bottom:4.6px">Data Tunneling</li>
    <li>Security</li>
  </ul>
  <h2 class="abs h h-white" style="left:15px;top:183px">Emberline Hardware Line</h2>
  <ul class="abs list list-w" style="left:9px;top:199px;width:130px;font-size:3.6px;line-height:1.2">
    <li style="margin-bottom:4.6px">PAC Controllers</li>
    <li style="margin-bottom:4.6px">Motion Control</li>
    <li style="margin-bottom:4.6px">Control Software Machine Edition</li>
    <li style="margin-bottom:4.6px">Industrial Ethernet switches</li>
    <li style="margin-bottom:4.6px">Human Machine Interfaces</li>
    <li style="margin-bottom:4.6px">Edge Device &amp; Software</li>
    <li>Safety Control</li>
  </ul>
  <div class="photo photo-grey framed" style="left:148px;top:56px;width:58px;height:58px" role="img" aria-label="Process plant piping"></div>
  <div class="photo photo-blue framed" style="left:148px;top:120px;width:58px;height:57px" role="img" aria-label="Blue robotic assembly cell"></div>
  <div class="photo framed" style="left:148px;top:183px;width:58px;height:58px;background:radial-gradient(circle at 50% 75%,rgba(240,190,110,.85),transparent 40%),linear-gradient(180deg,#6e86c0,#a58fb3 50%,#3d4d6e)" role="img" aria-label="Refinery at dusk"></div>
  <div class="abs" style="left:0;top:273px;width:180px;height:35px;background:var(--white)"></div>
  <p class="abs" style="left:15px;top:286px;font-size:7.5px;font-weight:600;color:var(--navy)">ORVANA</p>
  <p class="abs" style="left:75px;top:286px;font-size:7px;font-weight:600;color:var(--navy)">Linkware</p>
  <p class="abs" style="left:132px;top:286px;font-size:6px;font-weight:600;color:var(--navy)">EMBERLINE</p>
  <div class="abs fill-sky" style="left:0;top:308px;width:180px;height:13px"></div>
</section>

<section class="page" style="left:622px;top:455px">
  <h2 class="abs h" style="left:16px;top:13px">Success stories</h2>
  <div class="quote q-sky" style="top:27px;height:24px"><p>"And the results that I have had with ZentaLOOM have been satisfactory. The truth is, I trust the engineers who are on duty ".</p><b>Tomás Rivas, Automation Supervisor. HARVESTAR</b></div>
  <div class="quote q-pale" style="top:55px;height:35px"><p>"ZentaLOOM not to mention. They are almost, almost anytime we talk to them, in terms of service and parts.<br>Equipment failure is one of the problems and over time they (ZentaLOOM) have given us a very good response in plants that we have in Mexico ".</p><b>Marco Ledesma, Head of Automation and Control, GRANOVA</b></div>
  <div class="quote q-sky" style="top:95px;height:23px"><p>"It is easier to enter the computer, the program, the fault directly. Much faster than searching manually "</p><b>Vexa Mine</b></div>
  <div class="quote q-pale" style="top:123px;height:24px"><p>" We are dedicated to making electromechanical installations for different industries. Basically it is the pharmaceutical, cosmetic and food industry "</p><b>Raúl Montoya, Sales Manager of Allied Engineering in Plant Constructions</b></div>
  <div class="quote q-sky" style="top:153px;height:22px"><p>"They did not limit themselves to fixing the platform but they went much further."</p><b>Iván Ferraz, Costera Management</b></div>
  <div class="abs fill-sky" style="left:0;top:179px;width:241px;height:14px"></div>
  <div class="photo" style="left:0;top:193px;width:241px;height:148px;background:radial-gradient(circle at 55% 45%,rgba(200,230,250,.75),transparent 30%),radial-gradient(circle at 85% 80%,rgba(120,160,200,.6),transparent 40%),linear-gradient(160deg,#4f5a68,#7d8fa3 55%,#3f6f96)" role="img" aria-label="Hand touching tablet under holographic globe"></div>
  <div class="abs fill-navy" style="left:0;top:327px;width:72px;height:14px"></div>
</section>

<section class="page" style="left:905px;top:455px">
  <div class="photo" style="left:0;top:0;width:138px;height:238px;background:radial-gradient(ellipse at 60% 50%,rgba(110,210,230,.7),transparent 35%),radial-gradient(ellipse at 65% 10%,rgba(170,230,245,.6),transparent 30%),linear-gradient(180deg,#0b2a3f,#1b5a78 55%,#2b7d9c)" role="img" aria-label="Data center server corridor"></div>
  <div class="abs fill-sky" style="left:0;top:238px;width:138px;height:16px"></div>
  <p class="abs brand" style="left:148px;top:269px;font-size:8.5px">ZentaLOOM</p>
  <p class="abs txt" style="left:148px;top:295px;width:85px;line-height:1.25">Monterrey, NL<br>Calle Aurora # 218, Col. Mirador<br>Email: hola@zentaloom-mx.com</p>
  <p class="abs txt" style="left:148px;top:313px">Phone: +52 81 5550 0142</p>
  <p class="abs txt" style="left:148px;top:323px">www.zentaloom-mx.com</p>
</section>

</body>
</html>
```